Flyer-Design für Buchhaltungsservice
Zielgruppe
Wir bieten Buchhaltungservice und Lohnbuchhaltungsservice an und möchten damit Kleinunternehmen ansprechen!
Aufgabenstellung
Ich habe ein Text zusammengestellt , dieser kann ergänzt oder geändert werden! Bin für Ideen offen! Diesen Text nutze ich aber schon sehr lange! Ich würde vl. noch die Unterschrift mit einfügen als Abspann! Ich bin am überlegen ob ich ein Foto von mir selbst einfüge, aber das alles würde ich gerne durch den Designer als Vorschlag haben. Bitte bei meinem Bild auch ein Ausschnitt verwenden, das Bild ist absolut unbearbeitet! Gerne auch schwarz/weiß!
Die Sterne müssen bei dem Wort dabei stehen und ganz unten findet sich die Erklärung, dies ist rechtlich sehr wichtig!
Es sollte ein Flyer gestaltet werden was später als Postkarte versendet werden kann siehe Anlage von morvadruck datenblatt, bitte so ein Flyer gestalten!

```html
<!DOCTYPE html>
<html lang="de">
<head>
<meta charset="utf-8">
<title>ZAHLWERK GmbH – Buchhaltung</title>
<link rel="stylesheet" href="https://fonts.googleapis.com/css2?family=Open+Sans:ital,wght@0,400;0,600;1,400&display=swap">
<style>
  :root {
    --brand-blue: #1070b8;
    --panel-blue: #bfcdea;
    --text-dark: #3a3a3a;
    --white: #ffffff;
  }
  * { margin: 0; padding: 0; box-sizing: border-box; }
  html, body { width: 1120px; height: 1200px; overflow: hidden; background: var(--white); }
  body { font-family: "Open Sans", Arial, sans-serif; color: var(--text-dark); position: relative; }
  h1, h2 { font-weight: 400; }

  .claim-band {
    position: absolute; left: 0; top: 0; width: 1120px; height: 72px;
    background: var(--brand-blue); color: var(--white);
    font-size: 35px; letter-spacing: 0.5px; padding-left: 54px;
    display: flex; align-items: center; justify-content: center; gap: 22px;
  }
  .claim-dot { font-size: 20px; }

  .portrait {
    position: absolute; left: 0; top: 72px; width: 618px; height: 526px;
    background: linear-gradient(120deg, #d9d9d9 0%, #f2f2f2 35%, #bcbcbc 60%, #6b6b6b 85%, #3d3d3d 100%);
  }

  .brand-box {
    position: absolute; left: 316px; top: 72px; width: 245px; height: 110px;
    background: var(--brand-blue); color: var(--white);
    display: flex; flex-direction: column; align-items: center; justify-content: center; gap: 10px;
  }
  .brand-square { width: 28px; height: 28px; background: var(--white); }
  .brand-name { font-size: 22px; letter-spacing: 0.5px; white-space: nowrap; }

  .service-panel {
    position: absolute; left: 561px; top: 72px; width: 559px; height: 110px;
    background: var(--panel-blue); text-align: center;
  }
  .service-title { color: var(--brand-blue); font-size: 40px; line-height: 1.2; margin-top: 6px; padding-left: 20px; }
  .service-list { font-size: 21px; color: #404040; margin-top: 2px; white-space: nowrap; }
  .service-note { font-size: 13px; font-style: italic; position: absolute; right: 120px; top: 88px; }

  .story {
    position: absolute; left: 642px; top: 193px; width: 470px; font-size: 17px; line-height: 24px;
  }
  .lead { color: var(--brand-blue); font-style: italic; font-size: 22px; line-height: 28px; }
  .story .lead { white-space: nowrap; margin: 0 0 21px; }
  .story p { margin-bottom: 11px; }
  .story p + .lead { margin-top: 5px; }
  .story .lead-final { margin-top: 8px; }

  .offer { position: absolute; left: 65px; top: 615px; width: 600px; font-size: 17px; line-height: 24px; }
  .offer .lead { margin-bottom: 9px; }
  .offer-list { list-style: none; }
  .offer-list li { padding-left: 19px; position: relative; }
  .offer-list li::before { content: "•"; color: var(--brand-blue); position: absolute; left: 0; }
  .offer .closing { margin-top: 10px; }

  .sign-off { position: absolute; left: 65px; top: 900px; }
  .greeting { font-size: 17px; }
  .signer { font-size: 23px; margin-top: 2px; }
  .signature {
    position: absolute; left: 290px; top: 892px; width: 140px; height: 82px;
    background: linear-gradient(90deg, #f4f4f4, #e6e6e6);
  }

  .footnote { position: absolute; left: 65px; top: 984px; width: 600px; font-size: 7.4px; color: #555; letter-spacing: -0.25px; white-space: nowrap; overflow: hidden; }

  .contact-band {
    position: absolute; left: 0; top: 1004px; width: 688px; height: 120px;
    background: var(--brand-blue); color: var(--white);
  }
  .contact-brand {
    position: absolute; left: 8px; top: 16px; width: 182px;
    display: flex; flex-direction: column; align-items: center; gap: 12px;
  }
  .contact-brand .brand-name { font-size: 20px; }
  .contact-details { position: absolute; left: 209px; top: 13px; font-size: 17px; line-height: 24px; font-style: normal; white-space: nowrap; }

  .address-field { position: absolute; left: 714px; top: 940px; font-size: 20px; line-height: 28px; color: #222; }
</style>
</head>
<body>
  <header class="claim-band">
    <span>ZUVERLÄSSIG</span><span class="claim-dot">●</span><span>DISKRET</span><span class="claim-dot">●</span><span>PROFESSIONELL</span>
  </header>

  <div class="portrait" role="img" aria-label="Schwarz-weiß-Foto des Buchhalters am Schreibtisch mit goldenem Kerzenleuchter"></div>

  <div class="brand-box">
    <span class="brand-square"></span>
    <span class="brand-name">ZAHLWERK GmbH</span>
  </div>

  <section class="service-panel">
    <h1 class="service-title">Buchhaltung</h1>
    <p class="service-list">•&nbsp; mit Hol- und Bringservice &nbsp;•&nbsp; lfd. Lohnbuchhaltung</p>
    <span class="service-note">(auch Baulohn)</span>
  </section>

  <section class="story">
    <h2 class="lead">Mit Sicherheit kennen Sie die Situation:</h2>
    <p>Sie bekommen die Buchhaltungsunterlagen zurück und es fehlt die Zeit diese zu besprechen!</p>
    <p>Vermissen Sie nicht auch manchmal die persönliche Betreuung?</p>
    <h2 class="lead">Dann stellen Sie sich folgende Situation vor:</h2>
    <p>Ihr persönlicher Buchhalter* holt die Unterlagen<br>kostenlos durch einen Kurier bei Ihnen ab,<br>bucht sie und druckt anschließend die entsprechenden<br>betriebswirtschaftlichen Belege aus und<br>Sie bekommen die Auswertungen ausführlich erläutert.</p>
    <h2 class="lead lead-final">Dieser Service ist möglich!</h2>
  </section>

  <section class="offer">
    <h2 class="lead">Rufen Sie mich noch heute an, um so schnell wie möglich von<br>meinen Leistungen zu profitieren:</h2>
    <ul class="offer-list">
      <li>Ein Dienstleister für das Buchen der lfd. Geschäftsvorfälle<br>der Finanzbuchhaltung und lfd. Lohnbuchhaltung</li>
      <li>Immer gleicher Ansprechpartner</li>
      <li>Persönliche und qualifizierte Betreuung</li>
      <li>Hol- und Bringservice</li>
      <li>auch komplett digitale Buchhaltung* möglich</li>
    </ul>
    <h2 class="lead closing">Sie haben endlich eine Buchhalter* als Ansprechpartner, der<br>Sie sofort entlastet.</h2>
  </section>

  <div class="sign-off">
    <p class="greeting">Mit freundlichen Grüßen</p>
    <p class="signer">Anton Keller</p>
  </div>
  <div class="signature" role="img" aria-label="Handschriftliche Unterschrift"></div>

  <p class="footnote">*Mein Dienstleistungsangebot in der Buchhaltung umfasst ausschließlich das Buchen lfd. Geschäftsvorfälle, die lfd. Lohnabrechnung und das Fertigen der Lohnsteueranmeldung</p>

  <footer class="contact-band">
    <div class="contact-brand">
      <span class="brand-square"></span>
      <span class="brand-name">ZAHLWERK GmbH</span>
    </div>
    <address class="contact-details">
      ZAHLWERK GmbH<br>
      Lindenhofweg 12 &nbsp;•&nbsp; 72070 Tübingen<br>
      Telefon: 0151 / 000 417 26 &nbsp;•&nbsp; Email: info@zahlwerk.de<br>
      www.zahlwerk.de
    </address>
  </footer>

  <div class="address-field">
    FIrma<br>Firma 2<br>Vorname Nachname<br>Straße<br>Ort<br>Land
  </div>
</body>
</html>
```